Debt Relief Landing Page Design

I need a landing page designed (and the accompanying Thank You page) for my client.

I have drafted the wireframes for the layout of the pages (attached) and need a professional looking finish.

The main colours to use are green and blue as per their current branding, see website for specifications - http://www.clearpathledger.com.au/

Industry/Entity Type

Debt

Coding

Coded - Design and coding required

```html
<!DOCTYPE html>
<html lang="en">
<head>
<meta charset="utf-8">
<title>Clear Path Ledger – Debt Relief</title>
<link href="https://fonts.googleapis.com/css2?family=Roboto+Condensed:wght@400;700&family=Roboto+Slab:wght@400&family=Open+Sans:wght@400;600&display=swap" rel="stylesheet">
<style>
:root{
  --navy:#172d57;
  --navy-deep:#12264b;
  --green:#5e9631;
  --green-bright:#64a130;
  --green-text:#5c9a2c;
  --hero-grey:#4c4c4c;
  --header-bg:#f8f8f8;
  --field-bg:#e4e4e4;
  --white:#ffffff;
}
*{margin:0;padding:0;box-sizing:border-box}
html,body{width:824px;height:1200px;overflow:hidden;background:var(--white)}
body{position:relative;font-family:"Open Sans",Arial,sans-serif}
.abs{position:absolute}

/* header */
.site-header{left:0;top:0;width:824px;height:72px;background:var(--header-bg);border-top:2px solid #9a9a9a;border-bottom:2px solid var(--green)}
.brand{left:53px;top:20px;font-family:"Roboto Condensed",sans-serif;font-weight:700;font-size:30px;color:var(--navy);letter-spacing:-.5px;white-space:nowrap}
.call{left:638px;top:30px}
.call-label{left:667px;top:27px;font-family:"Roboto Slab",serif;font-size:11px;color:var(--green-text)}
.call-number{left:667px;top:40px;font-family:"Roboto Condensed",sans-serif;font-size:18px;color:var(--green-text);font-weight:400}

/* hero */
.hero{left:0;top:72px;width:824px;height:302px;background:var(--hero-grey);border-bottom:3px solid var(--green)}
.hero-photo{left:0;top:72px;width:220px;height:299px;background:linear-gradient(90deg,#6d6a66 0%,#5a5754 60%,rgba(76,76,76,0) 100%)}
.hero-title{left:176px;top:92px;width:360px;font-family:"Roboto Condensed",sans-serif;font-weight:400;font-size:29px;line-height:32px;color:var(--white)}
.hero-text{left:176px;width:355px;font-family:"Roboto Condensed",sans-serif;font-size:12px;line-height:16px;color:var(--white)}
.hero-text.last{width:295px}
.pointer{left:486px;top:330px}

/* form */
.consult{left:540px;top:76px;width:230px;height:296px;background:#dcdcdc;border:3px solid var(--navy)}
.consult-head{height:64px;background:var(--green);padding:3px 6px}
.consult-head h2{font-family:"Roboto Slab",serif;font-weight:400;font-size:21px;color:var(--white);border-bottom:1px dashed #c7dcb4;padding-bottom:2px}
.consult-head p{font-family:"Roboto Slab",serif;font-size:10px;line-height:14px;color:#2d4d14;margin-top:4px}
.field{position:absolute;left:5px;width:214px;height:19px;background:var(--field-bg);border:1px solid #888;font-family:"Roboto Slab",serif;font-size:10px;color:#333;padding:2px 6px}
.btn-small{position:absolute;left:14px;top:246px;width:200px;height:31px;background:var(--green-bright);color:var(--white);font-family:"Roboto Slab",serif;font-size:13px;text-align:center;line-height:31px;white-space:nowrap}

/* services */
.services{left:0;top:374px;width:824px;height:536px;background:var(--navy)}
.section-title{width:824px;left:0;text-align:center;font-family:"Roboto Slab",serif;font-weight:400;color:var(--white);font-size:19px}
.dash{height:0;border-top:1px dashed #b8c4d8}
.service{width:210px;text-align:center;color:var(--white)}
.service .icon{width:61px;height:61px;border-radius:50%;background:var(--white);margin:0 auto 11px;display:flex;align-items:center;justify-content:center}
.service h3{font-family:"Roboto Slab",serif;font-weight:400;font-size:13px;margin-bottom:16px}
.service p{font-size:11.5px;line-height:16px}
.btn-large{left:265px;top:838px;width:334px;height:59px;background:var(--green-bright);color:var(--white);font-family:"Roboto Slab",serif;font-size:22px;text-align:center;line-height:59px;border-radius:2px;white-space:nowrap}

/* testimonials */
.reviews{left:0;top:910px;width:824px;height:250px;background:var(--green);border-top:2px solid #e8e8e8}
.hex{clip-path:polygon(50% 0,100% 25%,100% 75%,50% 100%,0 75%,0 25%);background:var(--white)}
.hex-inner{clip-path:polygon(50% 0,100% 25%,100% 75%,50% 100%,0 75%,0 25%);background:linear-gradient(#d9d2c8,#a89c8e)}
.bubble{width:232px;height:96px;background:#6ba03c;border:1px solid #7cb04e;border-radius:3px;padding:8px 9px 0 10px;font-family:Arial,sans-serif;font-size:9.6px;line-height:13px;color:var(--white)}
.bubble .q{font-family:Georgia,serif;font-size:26px;color:#a5c985;float:left;line-height:20px;margin-right:4px;height:14px}
.bubble-tail{width:12px;height:12px;background:#6ba03c;border-right:1px solid #7cb04e;border-bottom:1px solid #7cb04e;transform:rotate(45deg)}
.reviewer{font-family:Arial,sans-serif;font-size:11.5px;color:var(--white)}

.site-footer{left:0;top:1160px;width:824px;height:40px;background:var(--navy-deep);text-align:center;line-height:40px;font-size:9.5px;font-weight:600;color:var(--white)}
.site-footer span{margin:0 4px}
</style>
</head>
<body>

<header class="site-header abs"></header>
<div class="brand abs">Clear Path Ledger</div>
<svg class="call abs" width="24" height="24" viewBox="0 0 24 24"><circle cx="12" cy="12" r="11" fill="none" stroke="#172d57" stroke-width="1.5"/><path d="M9 6c-1 1-2 3 0 7s4 5.5 5.5 5.5l1.5-1.5-2-2.5-1.5 1c-1-.5-2.5-2.5-3-4l1-1L9.5 6z" fill="#172d57"/></svg>
<div class="call-label abs">Call Us Today</div>
<div class="call-number abs">1300 555 014</div>

<section class="hero abs"></section>
<div class="hero-photo abs" role="img" aria-label="Photo of a smiling professional man at a desk"></div>
<h1 class="hero-title abs">Looking to Consolidate Your Debts?</h1>
<p class="hero-text abs" style="top:172px">If you have over $10,000 In Debt, We Can Help you be Debt free in 3-5 Years.</p>
<p class="hero-text abs" style="top:213px">Clear Path Ledger in Australia's debt help relief specialists. Through years fo industry experience and knowledge, our team of debt management experts can actively advise you on how to get our of the red, fast.</p>
<p class="hero-text abs" style="top:287px">At Clear Path Ledger we are able to actively rectify your debt problems by creating simple and affordable payment plans for all debts.</p>
<p class="hero-text last abs" style="top:327px">For a free, no obligation consultation simply fill out the form on the right and we'll be in contact with you shortly.</p>
<svg class="pointer abs" width="66" height="32" viewBox="0 0 70 32"><path d="M2 8 L44 10 L44 2 L66 16 L44 30 L44 22 L4 24 L8 16 Z" fill="none" stroke="#fff" stroke-width="1.5" stroke-linejoin="round"/></svg>

<form class="consult abs">
  <div class="consult-head">
    <h2>Free Consultaion</h2>
    <p>Fill In The Form Below To Recieve Your Free, No Obligation Consulation</p>
  </div>
  <div class="field" style="top:70px">Name</div>
  <div class="field" style="top:99px">Phone</div>
  <div class="field" style="top:129px">Email</div>
  <div class="field" style="top:158px">PostCode</div>
  <div class="field" style="top:188px">Unsecured Debt.</div>
  <div class="field" style="top:216px">Preferred Call Time</div>
  <div class="btn-small">GET MY FREE CONSTULATION</div>
</form>

<section class="services abs"></section>
<h2 class="section-title abs" style="top:391px">Here Are just Some Of Our Debt Relief Services</h2>
<div class="dash abs" style="left:205px;top:418px;width:415px"></div>

<div class="service abs" style="left:55px;top:448px">
  <div class="icon"><svg width="34" height="34" viewBox="0 0 34 34"><circle cx="20" cy="8" r="5" fill="none" stroke="#172d57" stroke-width="2"/><path d="M18 8v12l-4-3-3 2 7 10h8l3-8v-6l-3-1-2 1v-7z" fill="#172d57"/></svg></div>
  <h3>Debt Consolidation Loans</h3>
  <p>Stop Getting hassed by creditors.Let us consolidate your personal debts into an easy repayment plan.</p>
</div>
<div class="service abs" style="left:314px;top:448px">
  <div class="icon"><svg width="36" height="34" viewBox="0 0 36 34"><path d="M18 3 L33 17 H29 V31 H7 V17 H3 Z" fill="#172d57"/><text x="18" y="28" text-anchor="middle" font-family="Arial" font-weight="700" font-size="14" fill="#fff">$</text></svg></div>
  <h3>Mortage Refinance</h3>
  <p>Consolidate your debt into available home loan equity, signnifically reducing your general repayment</p>
</div>
<div class="service abs" style="left:558px;top:448px">
  <div class="icon"><svg width="40" height="30" viewBox="0 0 40 30"><rect x="3" y="4" width="28" height="22" rx="2" fill="none" stroke="#172d57" stroke-width="2"/><path d="M8 10h18M8 15h18M8 20h12" stroke="#172d57" stroke-width="2"/><path d="M26 22 L37 9 L39 11 L28 24 L25 25Z" fill="#172d57"/></svg></div>
  <h3>Debt Agreements</h3>
  <p>A viable alternative to bankruptcy and debt consolidtaions loans</p>
</div>

<div class="service abs" style="left:55px;top:637px">
  <div class="icon"><svg width="34" height="34" viewBox="0 0 34 34"><path d="M4 14 L14 30 L30 6 L24 8 L14 22 L10 12Z" fill="#172d57"/><path d="M16 4v12M21 3v10M26 2v8" stroke="#172d57" stroke-width="3"/></svg></div>
  <h3>Credit Repair</h3>
  <p>Assist you in removing unfair, disputable and incorrect information from your credit file / information, which you believe should not be there</p>
</div>
<div class="service abs" style="left:314px;top:637px">
  <div class="icon"><svg width="34" height="34" viewBox="0 0 34 34"><rect x="4" y="10" width="4" height="20" fill="#172d57"/><rect x="10" y="14" width="4" height="16" fill="#172d57"/><rect x="16" y="18" width="4" height="12" fill="#172d57"/><path d="M22 12v16l-3-3M22 28l3-3" stroke="#172d57" stroke-width="2" fill="none"/><text x="27" y="13" text-anchor="middle" font-family="Arial" font-weight="700" font-size="12" fill="#172d57">$</text></svg></div>
  <h3>Bankruptcy</h3>
  <p>We will work with you yo accuartely determine if bankruptcy is the sole option of your situation</p>
</div>
<div class="service abs" style="left:558px;top:637px">
  <div class="icon"><svg width="34" height="34" viewBox="0 0 34 34"><rect x="23" y="4" width="7" height="14" fill="#172d57"/><path d="M21 4H9L5 17h9l-2 10 3 2 6-11z" fill="#172d57"/></svg></div>
  <h3>Bad Credit Loans</h3>
  <p>We Work in your best interests to provide a consilidtaion loan that turns yourbad credit history into a positive financial situation</p>
</div>

<div class="btn-large abs">GET MY FREE CONSTULATION</div>

<section class="reviews abs"></section>
<h2 class="section-title abs" style="top:932px;font-size:16px">We Make Our Clients' Happy</h2>
<div class="dash abs" style="left:252px;top:973px;width:321px;border-color:#a9c98c"></div>

<svg class="abs" style="left:20px;top:1050px" width="20" height="32" viewBox="0 0 20 32"><path d="M17 2 L3 16 L17 30" fill="none" stroke="#fff" stroke-width="2"/></svg>
<svg class="abs" style="left:770px;top:1050px" width="20" height="32" viewBox="0 0 20 32"><path d="M3 2 L17 16 L3 30" fill="none" stroke="#fff" stroke-width="2"/></svg>

<div class="hex abs" style="left:55px;top:1010px;width:82px;height:82px"></div>
<div class="hex-inner abs" role="img" aria-label="Portrait of a client" style="left:58px;top:1013px;width:76px;height:76px"></div>
<div class="bubble-tail abs" style="left:164px;top:1094px"></div>
<div class="bubble abs" style="left:146px;top:1004px"><span class="q">&ldquo;</span>We were on the verge of losing our car &amp; did not know what to do, but now we are in an affordable arrangement to catch up our car payments and are on our way to a debt free future. We are even thinking of buying a house, without your help this would not be possible.</div>
<div class="reviewer abs" style="left:162px;top:1118px">Janelle, Box Hill, VIC</div>

<div class="hex abs" style="left:431px;top:1010px;width:82px;height:82px"></div>
<div class="hex-inner abs" role="img" aria-label="Portrait of a client" style="left:434px;top:1013px;width:76px;height:76px"></div>
<div class="bubble-tail abs" style="left:540px;top:1094px"></div>
<div class="bubble abs" style="left:522px;top:1004px"><span class="q">&ldquo;</span>We were on the verge of losing our car &amp; did not know what to do, but now we are in an affordable arrangement to catch up our car payments and are on our way to a debt free future. We are even thinking of buying a house, without your help this would not be possible.</div>
<div class="reviewer abs" style="left:538px;top:1118px">Janelle, Box Hill, VIC</div>

<footer class="site-footer abs"><span>&copy; 2015 ClearPathLedger. All Rights Reserved</span><span>Privacy Policy</span><span>Terms &amp; Conditions</span></footer>

</body>
</html>
```